Legislative compliance to home owners, landlords and agents

Logo, business card and stationaly header for a sole trader offering sevices in the UK to home owners, landlords and Letting agents to meet legislation requirement relating to sale and leasing of rental domestic homes. Services offered include Legionella Risk Assessment, Portable Appliance Testing and Energy Performance Certificates. Logo to include depiction of a house and compliance tick list images. Have an existing card with water splash image to reflect water testing, so considering picking up same wave blue. Company name Kestov Property Services. Web www.kestovps-example.com. email: info@kestovps-example.com. Address: Brackenlea, Aberdeen. All three services to be listed. Name as existing card.,

Target Market(s)

UK home owners, landlords, lettings and estate agents

Industry/Entity Type

Property Management

Contact Information for Business Card

Derek Moffatt CEng, MSFabTec
Address: Brackenlea, Aberdeen
Web: www.kestovps-example.com
e-mail info@kestovps-example.com
Phone: 07700 918 302
Services: Legionella Risk Assessment, Portable Appliance Testing, Energy Performance Certificate

Logo Text

Kestov Property Services

Font styles to use
Sans Serif

Colors

Designer to choose colors to be used in the design.

Requirements
Must have
• Suitable for standard UK business card size 85 mm x 55 mm, with allowance for safety border/ bleed such that colours extend to outside border of card once printed
Nice to have
• Clear font style and layout
• Happy to see images depicting phone, address etc

```html
<!DOCTYPE html>
<html lang="en">
<head>
<meta charset="utf-8">
<title>Kestov Property Services – Business Card</title>
<link rel="stylesheet" href="https://fonts.googleapis.com/css2?family=Arimo:wght@400;700&family=Lexend:wght@500&family=Varela+Round&display=swap">
<style>
  :root {
    --navy: #1f2a5e;
    --cyan: #29a8e0;
    --white: #ffffff;
    --ink: #111111;
    --stage: #000000;
  }
  * { margin: 0; padding: 0; box-sizing: border-box; }
  html, body {
    width: 976px; height: 1200px; overflow: hidden;
    background: var(--stage);
  }
  .card {
    position: absolute; left: 148px; width: 680px; height: 389px;
    background: var(--white); overflow: hidden;
  }
  .card--front { top: 126px; }
  .card--back { top: 665px; }

  .holder { position: absolute; left: 406px; top: 62px; }
  .holder__name {
    font-family: "Lexend", sans-serif; font-weight: 500;
    font-size: 26px; letter-spacing: -0.6px; color: var(--navy); line-height: 1.1;
  }
  .holder__credentials {
    font-family: "Varela Round", sans-serif; font-size: 20px;
    color: var(--cyan); margin-left: 7px; margin-top: 2px; letter-spacing: 0.3px;
  }

  .services-band {
    position: absolute; left: 2px; right: 0; top: 133px; height: 49px;
    background: var(--navy); color: var(--white);
    font-family: "Arimo", sans-serif; font-size: 15.6px;
    display: flex; align-items: center; padding-left: 20px;
  }

  .contacts { position: absolute; left: 55px; top: 216px; list-style: none; }
  .contacts__item {
    display: flex; align-items: center; height: 31px;
    font-family: "Arimo", sans-serif; font-size: 15.5px; color: var(--ink);
    letter-spacing: 0.2px;
  }
  .contacts__item--phone { font-size: 18.5px; }
  .contacts__icon { width: 23px; height: 23px; margin-right: 6px; flex: none; }

  .brand {
    position: absolute; display: flex; align-items: center; gap: 8px;
    font-family: "Arimo", sans-serif; font-weight: 700; color: var(--navy);
    white-space: nowrap;
  }
  .brand__mark { width: 14px; height: 14px; background: var(--cyan); border-radius: 50%; flex: none; }
  .brand--front { left: 316px; top: 286px; font-size: 22px; }

  .back-band { position: absolute; top: 192px; height: 49px; background: var(--navy); }
  .back-band--left { left: 0; width: 159px; }
  .back-band--right { left: 517px; right: 0; }
  .brand--back {
    left: 159px; width: 358px; top: 192px; height: 49px;
    justify-content: center; font-size: 21px;
  }
</style>
</head>
<body>
  <section class="card card--front">
    <div class="holder">
      <div class="holder__name">Derek Moffatt</div>
      <div class="holder__credentials">CEng, MSFabTec</div>
    </div>

    <div class="services-band">Legionella Risk Assessment, Portable Appliance Testing, Energy Performance Certificate</div>

    <ul class="contacts">
      <li class="contacts__item contacts__item--phone">
        <svg class="contacts__icon" viewBox="0 0 24 24" fill="none" stroke="var(--cyan)" stroke-width="1.5">
          <circle cx="12" cy="12" r="11"/><rect x="8.5" y="5.5" width="7" height="13" rx="1.2"/><line x1="11" y1="16.3" x2="13" y2="16.3"/>
        </svg>07700 918 302
      </li>
      <li class="contacts__item">
        <svg class="contacts__icon" viewBox="0 0 24 24" fill="none" stroke="var(--cyan)" stroke-width="1.5">
          <circle cx="12" cy="12" r="11"/><rect x="6" y="8" width="12" height="8.5"/><polyline points="6,8 12,13 18,8"/>
        </svg>e-mail info@kestovps-example.com
      </li>
      <li class="contacts__item">
        <svg class="contacts__icon" viewBox="0 0 24 24">
          <circle cx="12" cy="12" r="11" fill="none" stroke="var(--cyan)" stroke-width="1.5"/>
          <path d="M12 19s-5-5.2-5-8.6a5 5 0 0 1 10 0C17 13.8 12 19 12 19z" fill="var(--cyan)"/><circle cx="12" cy="10.4" r="1.9" fill="var(--white)"/>
        </svg>&nbsp;Brackenlea, Aberdeen
      </li>
      <li class="contacts__item">
        <svg class="contacts__icon" viewBox="0 0 24 24" fill="none" stroke="var(--cyan)" stroke-width="1.2">
          <circle cx="12" cy="12" r="11" stroke-width="1.5"/><circle cx="12" cy="12" r="6"/><ellipse cx="12" cy="12" rx="2.6" ry="6"/><line x1="6" y1="12" x2="18" y2="12"/>
        </svg>&nbsp;&nbsp;www.kestovps-example.com
      </li>
    </ul>

    <div class="brand brand--front"><span class="brand__mark"></span>Kestov Property Services</div>
  </section>

  <section class="card card--back">
    <div class="back-band back-band--left"></div>
    <div class="brand brand--back"><span class="brand__mark"></span>Kestov Property Services</div>
    <div class="back-band back-band--right"></div>
  </section>
</body>
</html>
```